**** Web design project for VornaSoft ****

For my ICT company VornaSoft I need a website.

We design, build and host web-applications and we have our own CMS product. In the references part we want to show sample websites (thumbnails) + links.

It should look modern (WEB 2.0), rounded corners.

I want the following menu' s:
- Home
- Services
- References
- News
- About VornaSoft
- Contact

Sample websites:
See attachments
http://www.plumvest.com
http://www.gadomirbureauwerk.nl

Reason: Want to take some time for feedback and improvements.

Reason: I'm waiting for a black background, with shadow and ambient light. You'll make a good chance!

Industry/Entity Type

It Company

Requirements
Must have
• - Fixed width (1024px), should fit on an IPad2
- Language selection English/Dutch
- Twitter/Facebook/LinkedIn/RSS icons
- Footer for Terms of use and Copyrights
- Search box
- 3 (or more) boxes for information i.e. news, blog or advertisements
Nice to have
• - Footer Site Map
- Contrasting background outside borders
- wide image (rotator) (with transperant sentence block)
- Shadow

```html
<!DOCTYPE html>
<html lang="en">
<head>
<meta charset="utf-8">
<title>VornaSoft – Web Applications &amp; CMS</title>
<link rel="stylesheet" href="https://fonts.googleapis.com/css2?family=Cinzel:wght@400;700&family=Questrial&display=swap">
<style>
:root{
  --navy-deep:#07131d;
  --navy:#0d2233;
  --navy-glow:#1d4868;
  --orange:#e8741e;
  --footer-top:#e58a2c;
  --footer-bottom:#d7701a;
  --paper:#ededed;
  --line:#d2d2d2;
  --text:#3a3a3a;
  --heading-blue:#1b4a6b;
  --link-blue:#1a7fd6;
  --white:#ffffff;
  --black:#0c0c0c;
}
*{box-sizing:border-box;margin:0;padding:0}
html,body{width:934px;height:1200px;overflow:hidden}
body{position:relative;background:var(--paper);font-family:"Questrial",Arial,sans-serif;color:var(--text)}
.abs{position:absolute}

/* header */
.site-header{position:absolute;left:0;top:0;width:934px;height:468px;
  background:radial-gradient(ellipse 520px 260px at 590px 250px,var(--navy-glow) 0%,var(--navy) 45%,var(--navy-deep) 100%)}
.top-tab{left:560px;top:0;width:270px;height:24px}
.search{left:601px;top:4px;width:134px;height:17px;display:flex}
.search-field{flex:1;background:#3d3d3d;color:#eee;font-size:8.5px;padding:3px 6px;border-radius:2px 0 0 2px;white-space:nowrap}
.search-btn{width:18px;background:var(--orange);border-radius:0 2px 2px 0}
.flag{top:6px;width:16px;height:11px}
.brand{left:110px;top:22px;display:flex;align-items:center;gap:12px}
.brand-mark{width:66px;height:66px;border-radius:50%;background:radial-gradient(circle at 40% 35%,#5fb3e6,#1a5f95 70%,#0f3656)}
.brand-name{font-size:31px;color:#a3b2bd;letter-spacing:.5px}
.main-nav{left:392px;top:45px;display:flex;font-size:11.5px;color:var(--white);white-space:nowrap}
.main-nav a{color:inherit;text-decoration:none;display:block;height:20px;line-height:20px}
.main-nav .current{background:linear-gradient(#f4f4f4,#c9c9c9);color:#222;border-radius:4px;padding:0 13px;margin-right:14px}
.hero-title{left:110px;top:138px;font-size:21px;font-weight:400;color:var(--orange)}
.hero-copy{left:113px;top:179px;font-size:11.3px;line-height:16px;color:#e9eef2;white-space:nowrap}
.btn-learn{left:110px;top:378px;width:108px;height:35px;border-radius:18px;
  background:linear-gradient(#f08a2e,#d5610d);border:2px solid #8a3a05;color:var(--white);
  font-size:15px;text-align:center;line-height:31px;letter-spacing:.3px}
.slide{background:linear-gradient(#f2f2f2 0%,#d83030 12%,#eeeeee 45%,#cfd8e0 70%,#f4f4f4 100%);box-shadow:0 6px 16px rgba(0,0,0,.6)}
.slide-side{opacity:.9}
.slider-tab{left:408px;top:437px;width:116px;height:31px}

/* content */
.section-title{font-family:"Cinzel",Georgia,serif;font-size:15.5px;font-weight:400;letter-spacing:.6px;color:#555}
.section-title b{color:var(--heading-blue)}
.rule{height:1px;background:var(--line)}
.intro{left:110px;top:516px;font-size:9.8px;line-height:14px;color:#333;white-space:nowrap}
.monitor{left:110px;top:556px;width:190px;height:162px;border-radius:6px;
  background:linear-gradient(#1d1d1d 0,#1d1d1d 4%,#dfe9ef 4%,#b9d27a 55%,#e8e8e8 80%,#1d1d1d 80%,#1d1d1d 86%,#cfcfcf 86%,#f2f2f2 100%)}
.features{left:318px;top:567px;list-style:none;font-size:10.4px;color:#444;white-space:nowrap}
.features li{height:17.4px;display:flex;align-items:center;gap:9px}
.bar{height:18px;border-radius:4px;background:linear-gradient(#e1e1e1,#d2d2d2);font-size:10px;color:#555;text-align:right;padding-right:8px;line-height:18px}
.news-item{left:638px;width:190px}
.news-photo{position:absolute;left:2px;top:0;width:50px;height:52px;border:1px solid #fff;box-shadow:0 0 2px rgba(0,0,0,.3);
  background:linear-gradient(160deg,#c8d6e2,#6b7d8c 60%,#2c3a46)}
.news-body{position:absolute;left:64px;top:0;width:126px;font-size:10.3px;line-height:11.8px;color:#444}
.news-body h3{font-weight:400;color:var(--link-blue);font-size:10.3px}
.news-more{position:absolute;left:64px;top:47px;font-size:9.3px;font-style:italic;color:#555}
.arrows{left:796px;top:770px;width:28px;height:14px}
.card{top:803px;width:130px;height:131px;background:#f8f8f8;border-radius:4px;box-shadow:0 1px 4px rgba(0,0,0,.35)}
.card-shot{position:absolute;left:3px;top:3px;width:124px;height:106px;
  background:linear-gradient(#cf1f1f 0,#cf1f1f 16%,#e9eef2 16%,#c7cfd6 55%,#f5f5f5 75%,#e8e8e8 100%)}
.card-url{position:absolute;left:3px;top:110px;width:124px;height:17px;background:#1a1a1a;color:#fff;font-size:10.2px;text-align:center;line-height:17px}

/* footer */
.site-footer{position:absolute;left:0;top:980px;width:934px;height:174px;background:linear-gradient(var(--footer-top),var(--footer-bottom))}
.foot-title{top:1000px;font-family:"Cinzel",Georgia,serif;font-size:11.5px;font-weight:700;color:var(--white);letter-spacing:.3px;white-space:nowrap}
.foot-list{top:1031px;list-style:none;font-size:10px;line-height:16px;color:#2a1605}
.foot-list.light{color:var(--white)}
.divider{top:1000px;width:1px;height:142px;background:rgba(120,55,0,.35)}
.input{left:109px;width:168px;height:22px;background:#fff;border-radius:6px;font-size:9.5px;color:#666;padding:5px 8px}
.btn-subscribe{left:197px;top:1100px;width:80px;height:22px;border-radius:11px;background:linear-gradient(#ffd24a,#f19a12);
  border:1px solid #a85d00;color:#fff;font-size:10.5px;text-align:center;line-height:20px}
.blog{left:637px;width:190px;font-size:10px;line-height:16px;color:#fff}
.blog em{color:#fff3e0}
.bottom-bar{left:0;top:1154px;width:934px;height:46px;background:var(--black)}
.copyright{left:110px;top:1167px;font-size:9.5px;color:#fff}
.social{top:1162px;width:23px;height:23px;border-radius:50%;background:#f3f3f3;border:1px solid #777}
</style>
</head>
<body>

<header class="site-header">
  <svg class="abs top-tab" viewBox="0 0 270 24" aria-hidden="true">
    <path d="M0 0 Q20 0 24 12 Q28 24 46 24 H224 Q242 24 246 12 Q250 0 270 0Z" fill="#f4f4f4"/>
  </svg>
  <div class="abs search"><span class="search-field">Enter your Keyword...</span><span class="search-btn"></span></div>
  <svg class="abs flag" style="left:752px" viewBox="0 0 16 11" role="img" aria-label="English">
    <rect width="16" height="11" fill="#233f8a"/><rect x="6.5" width="3" height="11" fill="#fff"/><rect y="4" width="16" height="3" fill="#fff"/>
    <rect x="7.2" width="1.6" height="11" fill="#c8202c"/><rect y="4.7" width="16" height="1.6" fill="#c8202c"/>
  </svg>
  <svg class="abs flag" style="left:778px" viewBox="0 0 16 11" role="img" aria-label="Dutch">
    <rect width="16" height="3.7" fill="#fff"/><rect y="3.7" width="16" height="3.6" fill="#2346a8"/><rect y="7.3" width="16" height="3.7" fill="#d52b1e"/>
  </svg>

  <div class="abs brand"><span class="brand-mark"></span><span class="brand-name">VornaSoft</span></div>

  <nav class="abs main-nav">
    <a class="current" href="#">Home</a>
    <a href="#" style="width:68px">Services</a>
    <a href="#" style="width:82px">References</a>
    <a href="#" style="width:54px">News</a>
    <a href="#" style="width:102px">About VornaSoft</a>
    <a href="#">Contact</a>
  </nav>

  <h1 class="abs hero-title">Welcome to VornaSoft</h1>
  <p class="abs hero-copy">Contrary to popular belief, Lorem Ipsum<br>is not simply random text. It has roots in<br>a piece of classical Latin literature from<br>45 BC, making it over 2000 years old.<br>Arvid Pellmore, a Latin professor at<br>Dunmore Hall College in Ohio,<br>looked up one of the more obscure Latin<br>words, consectetur, from a Lorem Ipsum<br>passage, and going through the cites of<br>the word in classical literature, discov-<br>ered the undoubtable source.</p>
  <div class="abs btn-learn">LEARN MORE</div>

  <div class="abs slide slide-side" style="left:342px;top:180px;width:98px;height:177px" role="img" aria-label="Sample website screenshot, left"></div>
  <div class="abs slide slide-side" style="left:722px;top:180px;width:98px;height:177px" role="img" aria-label="Sample website screenshot, right"></div>
  <div class="abs slide" style="left:438px;top:157px;width:285px;height:215px" role="img" aria-label="Featured sample website screenshot with business people"></div>

  <svg class="abs slider-tab" viewBox="0 0 116 31" aria-hidden="true">
    <path d="M0 31 Q4 3 24 2 H92 Q112 3 116 31Z" fill="var(--navy-deep)" stroke="#4d6a80"/>
    <circle cx="20" cy="14" r="5" fill="#e21b1b" stroke="#fff" stroke-width="1.5"/>
    <circle cx="38" cy="14" r="5.5" fill="#fff"/><circle cx="56" cy="14" r="5.5" fill="#fff"/>
    <circle cx="74" cy="14" r="5.5" fill="#fff"/><circle cx="92" cy="14" r="5.5" fill="#fff"/>
  </svg>
</header>

<main>
  <h2 class="abs section-title" style="left:110px;top:484px">WHY <b>OUR CMS ?</b></h2>
  <div class="abs rule" style="left:110px;top:506px;width:470px"></div>
  <p class="abs intro">Lorem ipsum dolor sit amet, consectetur adipiscing elit, sed do eiusmod tempor incididunt ut labore et<br>dolore magna aliqua. veniam, quillamco laboris nisi ut aliquip ex ea commodo consequat :-</p>
  <div class="abs monitor" role="img" aria-label="Desktop monitor showing a sample CMS website"></div>
  <ul class="abs features">
    <li><svg width="11" height="11" viewBox="0 0 11 11"><rect x=".5" y=".5" width="10" height="10" fill="#fff" stroke="#999"/><path d="M2 5.5l2.5 2.5L10 1" fill="none" stroke="#444" stroke-width="1.6"/></svg>Vivamus sit amet tellus ut metus blandit sapien.</li>
    <li><svg width="11" height="11" viewBox="0 0 11 11"><rect x=".5" y=".5" width="10" height="10" fill="#fff" stroke="#999"/><path d="M2 5.5l2.5 2.5L10 1" fill="none" stroke="#444" stroke-width="1.6"/></svg>Proin in metus eu augue feugiat placerat &nbsp;odio.</li>
    <li><svg width="11" height="11" viewBox="0 0 11 11"><rect x=".5" y=".5" width="10" height="10" fill="#fff" stroke="#999"/><path d="M2 5.5l2.5 2.5L10 1" fill="none" stroke="#444" stroke-width="1.6"/></svg>Quisque non orci id tortor blandit auctor amet.</li>
    <li><svg width="11" height="11" viewBox="0 0 11 11"><rect x=".5" y=".5" width="10" height="10" fill="#fff" stroke="#999"/><path d="M2 5.5l2.5 2.5L10 1" fill="none" stroke="#444" stroke-width="1.6"/></svg>Vestibulum eleifend libero odio, eleifend viverra</li>
    <li><svg width="11" height="11" viewBox="0 0 11 11"><rect x=".5" y=".5" width="10" height="10" fill="#fff" stroke="#999"/><path d="M2 5.5l2.5 2.5L10 1" fill="none" stroke="#444" stroke-width="1.6"/></svg>Proin pretium ligula ut massa pellentesque</li>
    <li><svg width="11" height="11" viewBox="0 0 11 11"><rect x=".5" y=".5" width="10" height="10" fill="#fff" stroke="#999"/><path d="M2 5.5l2.5 2.5L10 1" fill="none" stroke="#444" stroke-width="1.6"/></svg>Aliquam mollis malesuada dolor, sed placerat</li>
    <li><svg width="11" height="11" viewBox="0 0 11 11"><rect x=".5" y=".5" width="10" height="10" fill="#fff" stroke="#999"/><path d="M2 5.5l2.5 2.5L10 1" fill="none" stroke="#444" stroke-width="1.6"/></svg>Proin pretium ligula ut massa pellentesque</li>
    <li><svg width="11" height="11" viewBox="0 0 11 11"><rect x=".5" y=".5" width="10" height="10" fill="#fff" stroke="#999"/><path d="M2 5.5l2.5 2.5L10 1" fill="none" stroke="#444" stroke-width="1.6"/></svg>Aliquam mollis malesuada dolor, sed placerat</li>
  </ul>
  <div class="abs bar" style="left:110px;top:730px;width:470px">Read More ▸</div>

  <h2 class="abs section-title" style="left:638px;top:484px">LATEST <b>NEWS</b></h2>
  <div class="abs rule" style="left:638px;top:506px;width:184px"></div>
  <article class="abs news-item" style="top:519px;height:58px">
    <div class="news-photo" role="img" aria-label="News photo of a business team"></div>
    <div class="news-body"><h3>Contrary to popular</h3>Lorem Ipsum is not simply random text...</div>
    <span class="news-more">Read More...</span>
  </article>
  <article class="abs news-item" style="top:590px;height:58px">
    <div class="news-photo" role="img" aria-label="News photo of a business team"></div>
    <div class="news-body"><h3>Contrary to popular</h3>Lorem Ipsum is not simply random text...</div>
    <span class="news-more">Read More...</span>
  </article>
  <article class="abs news-item" style="top:661px;height:58px">
    <div class="news-photo" role="img" aria-label="News photo of a business team"></div>
    <div class="news-body"><h3>Contrary to popular</h3>Lorem Ipsum is not simply random text...</div>
    <span class="news-more">Read More...</span>
  </article>
  <div class="abs bar" style="left:638px;top:730px;width:184px">View All News ▸</div>

  <h2 class="abs section-title" style="left:110px;top:767px"><b>OUR CUSTOMERS</b></h2>
  <svg class="abs arrows" viewBox="0 0 28 14" aria-hidden="true">
    <path d="M8 2L3 7l5 5M20 2l5 5-5 5" fill="none" stroke="#555" stroke-width="2"/>
  </svg>
  <div class="abs rule" style="left:110px;top:790px;width:714px"></div>

  <div class="abs card" style="left:109px"><div class="card-shot" role="img" aria-label="Customer website thumbnail"></div><div class="card-url">www.sitenamehere.com</div></div>
  <div class="abs card" style="left:255px"><div class="card-shot" role="img" aria-label="Customer website thumbnail"></div><div class="card-url">www.sitenamehere.com</div></div>
  <div class="abs card" style="left:400px"><div class="card-shot" role="img" aria-label="Customer website thumbnail"></div><div class="card-url">www.sitenamehere.com</div></div>
  <div class="abs card" style="left:545px"><div class="card-shot" role="img" aria-label="Customer website thumbnail"></div><div class="card-url">www.sitenamehere.com</div></div>
  <div class="abs card" style="left:691px"><div class="card-shot" role="img" aria-label="Customer website thumbnail"></div><div class="card-url">www.sitenamehere.com</div></div>
</main>

<footer>
  <div class="site-footer"></div>
  <h3 class="abs foot-title" style="left:109px">SUBSCRIBE OUR NEWSLETTER!</h3>
  <div class="abs input" style="top:1034px">Enter Your Name</div>
  <div class="abs input" style="top:1062px">Enter Your Email Address</div>
  <div class="abs btn-subscribe">SUBSCRIBE</div>
  <div class="abs divider" style="left:310px"></div>

  <h3 class="abs foot-title" style="left:337px">QUICK LINKS</h3>
  <ul class="abs foot-list" style="left:337px">
    <li>Home</li><li>Services</li><li>References</li><li>News</li><li>About VornaSoft</li><li>Contact</li>
  </ul>
  <div class="abs divider" style="left:441px"></div>

  <h3 class="abs foot-title" style="left:469px">CONTACT US</h3>
  <ul class="abs foot-list light" style="left:469px">
    <li>Lorem ipsum dolor amet,</li><li>Consectetur adipiscing,</li><li>Contary popular,</li><li>Sit amet.</li>
    <li>Ph - 123 456 7890</li><li>Fax - 123 456 7890</li>
  </ul>
  <div class="abs divider" style="left:607px"></div>

  <h3 class="abs foot-title" style="left:637px">BLOG</h3>
  <div class="abs blog" style="top:1029px"><em>12 April 2012</em><br>Lorem ipsum dolor sit amet, consectetur adipiscing elit ...</div>
  <div class="abs rule" style="left:637px;top:1085px;width:188px;background:rgba(255,255,255,.45)"></div>
  <div class="abs blog" style="top:1093px"><em>12 April 2012</em><br>Lorem ipsum dolor sit amet, consectetur adipiscing elit ...</div>

  <div class="abs bottom-bar"></div>
  <p class="abs copyright">Copyright©2012 VornaSoft. All Rights Reserved.</p>
  <span class="abs social" style="left:709px" role="img" aria-label="Social link one"></span>
  <span class="abs social" style="left:740px" role="img" aria-label="Social link two"></span>
  <span class="abs social" style="left:771px" role="img" aria-label="Social link three"></span>
  <span class="abs social" style="left:801px" role="img" aria-label="News feed link"></span>
</footer>

</body>
</html>
```